YARD FRONTS "N" MORE

catyering to driveway/patio floor construction and remodeling. Concrete, concrete pavers, asphalt, Landscaping, irrigation, pergolas and pools.

Target Market(s)

the home owner that wants to enhance their home

Industry/Entity Type

construction

Contact Information for Business Card

presidet: tomas bellweather email: yardfrontsnmore@example.come office/cell: 555 214 8830

Font styles to use
Sans Serif

Requirements
Must have
• logo should pop out
Nice to have
• the logo should demonstrate that we do exteriors only

```html
<!DOCTYPE html>
<html lang="en">
<head>
<meta charset="UTF-8">
<title>Yard Fronts "N" More — Business Card</title>
<link rel="stylesheet" href="https://fonts.googleapis.com/css2?family=Montserrat:wght@300;400&display=swap">
<style>
  :root {
    --page-bg: #2b2b2c;
    --card-bg: #3d3d3f;
    --ink: #ffffff;
    --ink-soft: #e6e6e6;
  }
  * { margin: 0; padding: 0; box-sizing: border-box; }
  html, body {
    width: 1200px;
    height: 900px;
    overflow: hidden;
    background: var(--page-bg);
    font-family: "Montserrat", sans-serif;
    color: var(--ink);
  }
  .canvas { position: relative; width: 1200px; height: 900px; }
  .card {
    position: absolute;
    top: 301px;
    width: 514px;
    height: 296px;
    background: var(--card-bg);
    box-shadow: 0 6px 14px rgba(0,0,0,0.35);
  }
  .card--front { left: 73px; }
  .card--back { left: 615px; }

  .brand-mark {
    display: block;
    border: 2.5px solid var(--ink);
  }
  .brand-name {
    font-weight: 300;
    font-size: 18px;
    line-height: 24px;
    letter-spacing: 0.3px;
    color: var(--ink);
  }

  .front-brand {
    position: absolute;
    left: 0; right: 0; top: 94px;
    display: flex;
    flex-direction: column;
    align-items: center;
    text-align: center;
  }
  .front-brand .brand-mark { width: 48px; height: 48px; margin-bottom: 16px; }

  .back-brand {
    position: absolute;
    left: 38px; top: 36px;
    display: flex;
    align-items: center;
    gap: 14px;
  }
  .back-brand .brand-mark { width: 54px; height: 54px; }

  .contact-block { position: absolute; left: 50px; top: 170px; }
  .person-name {
    font-weight: 400;
    font-size: 23px;
    line-height: 28px;
    letter-spacing: 0.2px;
  }
  .person-title {
    font-weight: 400;
    font-size: 13px;
    letter-spacing: 0.5px;
    margin-top: 4px;
    color: var(--ink-soft);
  }
  .contact-list { list-style: none; margin-top: 24px; }
  .contact-item {
    display: flex;
    align-items: center;
    gap: 8px;
    font-size: 13.5px;
    line-height: 18px;
    color: var(--ink-soft);
  }
  .contact-icon { width: 12px; height: 10px; flex: none; fill: var(--ink-soft); }
</style>
</head>
<body>
<main class="canvas">
  <section class="card card--front" aria-label="Business card front">
    <div class="front-brand">
      <span class="brand-mark" aria-hidden="true"></span>
      <p class="brand-name">YARD FRONTS<br>'N' MORE</p>
    </div>
  </section>

  <section class="card card--back" aria-label="Business card back">
    <div class="back-brand">
      <span class="brand-mark" aria-hidden="true"></span>
      <p class="brand-name">YARD FRONTS<br>'N' MORE</p>
    </div>
    <div class="contact-block">
      <p class="person-name">tomas bellweather</p>
      <p class="person-title">PRESIDENT</p>
      <ul class="contact-list">
        <li class="contact-item">
          <svg class="contact-icon" viewBox="0 0 12 10" aria-label="Phone">
            <path d="M0 3.2C0 1.5 2.7 0.5 6 0.5s6 1 6 2.7v1H8.6V2.8H3.4v1.4H0z"/>
            <path d="M2.5 5h7l1.5 4.5H1z"/>
            <circle cx="6" cy="7" r="1.3" fill="#3d3d3f"/>
          </svg>
          <span>555 214 8830</span>
        </li>
        <li class="contact-item">
          <svg class="contact-icon" viewBox="0 0 12 10" aria-label="Email">
            <path d="M0 1h12v1.2L6 5.6 0 2.2z"/>
            <path d="M0 3.6l6 3.4 6-3.4V9H0z"/>
          </svg>
          <span>yardfrontsnmore@example.com</span>
        </li>
      </ul>
    </div>
  </section>
</main>
</body>
</html>
```